Advert for Services that we offer

Bolt Remova Ltd need an design to represent what we do in a modern way by showing an image with a brief description and the use of corporate logo the information we will proved vie a doc file and this is to be presented in a modern way. This design will be for print & web. we have done our own design and its not great i have put this in the file repository

Target Market(s)

Motor trade

Font styles to use
Sans Serif

Colors

Designer to choose colors to be used in the design.

Requirements
Must have
• Company colour scheme as per logo within the files uploaded.
• and a small boarder to isolate it from the rest of the articles.
Nice to have
• Modern font
Should not have
• Old style font

```html
<!DOCTYPE html>
<html lang="en">
<head>
<meta charset="utf-8">
<title>Bolt Remova Ltd – Product Testing and Analysis</title>
<link rel="stylesheet" href="https://fonts.googleapis.com/css2?family=Bebas+Neue&family=Montserrat:ital,wght@0,500;0,600;0,700;1,500&display=swap">
<style>
  :root {
    --brand-blue: #1f6db5;
    --brand-blue-deep: #17599a;
    --brand-blue-light: #2c7fcc;
    --ink-blue: #2a6fba;
    --white: #ffffff;
    --photo-grey: #8a8d90;
    --photo-dark: #3b4046;
    --photo-rust: #a8452a;
    --page: #e9ecef;
  }
  * { margin: 0; padding: 0; box-sizing: border-box; }
  html, body {
    width: 1200px; height: 775px; overflow: hidden;
    background: var(--page);
  }
  .advert {
    position: relative;
    width: 1200px; height: 775px;
    overflow: hidden;
    font-family: "Montserrat", Arial, sans-serif;
    color: var(--white);
  }
  .hero-photo {
    position: absolute; inset: 0;
    background:
      radial-gradient(ellipse 260px 240px at 880px 540px, var(--photo-rust) 0%, rgba(168,69,42,0.6) 45%, transparent 75%),
      radial-gradient(ellipse 220px 500px at 1100px 380px, var(--photo-dark) 0%, transparent 80%),
      linear-gradient(160deg, #c9cccf 0%, #9ea2a6 45%, var(--photo-grey) 70%, #6d7176 100%);
  }
  .shapes { position: absolute; inset: 0; }
  .brand {
    position: absolute; left: 62px; top: 66px;
    display: flex; align-items: center; gap: 10px;
    white-space: nowrap;
  }
  .brand-mark {
    flex: 0 0 auto;
    width: 26px; height: 26px;
    background: var(--ink-blue);
  }
  .brand-name {
    font-family: "Montserrat", Arial, sans-serif;
    font-weight: 700;
    font-size: 20px;
    letter-spacing: 0.4px;
    color: var(--ink-blue);
    line-height: 1;
  }
  .phone {
    position: absolute; left: 358px; top: 60px;
    font-family: "Montserrat", Arial, sans-serif;
    font-style: italic; font-weight: 500;
    font-size: 30px; letter-spacing: 0.5px;
    line-height: 36px;
    white-space: nowrap;
    color: var(--ink-blue);
  }
  .headline {
    position: absolute; left: 58px; top: 204px;
    font-family: "Bebas Neue", "Oswald", sans-serif;
    font-weight: 400;
    font-size: 84px; line-height: 73px;
    letter-spacing: 1.5px;
    white-space: nowrap;
  }
  .service-list {
    position: absolute; left: 68px; top: 370px;
    list-style: none;
  }
  .service-list li {
    position: relative;
    padding-left: 22px;
    font-size: 24px; font-weight: 500;
    line-height: 46px;
    letter-spacing: 0.3px;
    white-space: nowrap;
  }
  .service-list li::before {
    content: ""; position: absolute; left: 0; top: 20px;
    width: 8px; height: 8px; border-radius: 50%;
    background: var(--white);
  }
  .web-pill {
    position: absolute; left: 66px; top: 678px;
    width: 306px; height: 47px;
    border: 2px solid var(--white); border-radius: 24px;
    display: flex; align-items: center; justify-content: center;
    font-size: 19px; font-weight: 600; letter-spacing: 0.2px;
    white-space: nowrap;
  }
</style>
</head>
<body>
  <main class="advert">
    <div class="hero-photo" role="img" aria-label="Technician in safety glasses measuring the bore of a flanged red hub with a digital dial gauge in a workshop"></div>

    <svg class="shapes" width="1200" height="775" viewBox="0 0 1200 775" aria-hidden="true">
      <defs>
        <linearGradient id="panelBlue" x1="0" y1="0" x2="1" y2="1">
          <stop offset="0" stop-color="#226fb7"/>
          <stop offset="0.6" stop-color="#1e69af"/>
          <stop offset="1" stop-color="#1a5e9f"/>
        </linearGradient>
      </defs>
      <polygon points="0,0 645,0 607,162 0,162" fill="#ffffff"/>
      <polygon points="0,162 607,162 455,775 0,775" fill="url(#panelBlue)"/>
    </svg>

    <header>
      <div class="brand">
        <span class="brand-mark"></span>
        <span class="brand-name">BOLT REMOVA LTD</span>
      </div>
      <div class="phone">0161 555 0192</div>
    </header>

    <h1 class="headline">Product Testing<br>and Analysis</h1>

    <ul class="service-list">
      <li>Metallurgical Testing</li>
      <li>Bearing Pre-load Testing</li>
      <li>Bore Measurement</li>
      <li>New Product Evaluation</li>
      <li>Product Analysis &amp; Report</li>
    </ul>

    <div class="web-pill">www.bolt-remova.co.uk</div>
  </main>
</body>
</html>
```